Anzeigengestaltung für eine Hausarztpraxis
Zielgruppe
Wir sind eine Hausarztpraxis mit zwei Standorten und suchen eine Ärztin oder einen Arzt zur Anstellung in der klassischen Hausarzt Medizin am Standort Sonnhalden
Aufgabenstellung
Bitte beachtet den Text im Anhang, der ist schon vorgegeben. (Anzeigentext)
Wir suchen ein ruhiges, hochwertiges Layout für eine Stellenanzeige einer Hausarztpraxis in einem historischen Gebäude.
Der Text steht im Vordergrund, das Design soll zurückhaltend, klar und wertig sein.
Bitte keine Icons, keine bunten Farben, keine verspielten Elemente.
Gerne viel Weissraum, klare Typografie, ruhige Anmutung.
Schrift: Garamond für den Fliesstext (bereits gewählt).
Das Layout soll sowohl als PDF wie auch online funktionieren.
Optional: ein sehr dezentes grafisches Element oder eine ruhige Bildanmutung (z. B. Struktur, Licht, Architekturdetail).

```html
<!DOCTYPE html>
<html lang="de">
<head>
<meta charset="utf-8">
<title>Stellenanzeige Hausarztpraxis</title>
<link rel="stylesheet" href="https://fonts.googleapis.com/css2?family=EB+Garamond:wght@400;500;600;700&display=swap">
<style>
  :root {
    --canvas: #e4e4e2;
    --paper: #ffffff;
    --ink: #2b2b2b;
    --text: #5a5a5a;
    --accent: #8dbb2a;
    --footer-bg: #eef2e5;
    --band: rgba(60, 58, 55, 0.78);
    --photo-top: #e9e8e4;
    --photo-mid: #b9b4a8;
    --photo-bottom: #6f7a55;
  }
  * { margin: 0; padding: 0; box-sizing: border-box; }
  html, body { width: 1200px; height: 1200px; overflow: hidden; }
  body {
    background: var(--canvas);
    font-family: "EB Garamond", Garamond, serif;
    display: flex; align-items: center; justify-content: center;
  }
  .ad {
    position: relative;
    width: 821px; height: 1160px;
    background: var(--paper);
    overflow: hidden;
  }
  .hero {
    position: absolute; left: 0; top: 0; width: 821px; height: 375px;
    background: linear-gradient(180deg, var(--photo-top) 0%, #dcdad4 45%, var(--photo-mid) 70%, var(--photo-bottom) 100%);
  }
  .hero-band {
    position: absolute; left: 0; top: 283px; width: 741px; height: 92px;
    background: var(--band);
    color: #fff;
    padding: 10px 0 0 50px;
  }
  .hero-title { font-size: 34px; font-weight: 600; line-height: 1.05; letter-spacing: 0.2px; }
  .hero-sub { font-size: 33px; font-weight: 400; line-height: 1.1; white-space: nowrap; }
  .intro {
    position: absolute; left: 50px; top: 412px; width: 176px;
    border-top: 2px solid var(--accent);
    border-bottom: 2px solid var(--accent);
    padding: 12px 0 14px;
    color: var(--ink);
    font-size: 17.5px; line-height: 22px;
  }
  .intro p { margin-bottom: 6px; }
  .intro p.gap { margin-top: 12px; }
  .content {
    position: absolute; left: 268px; top: 406px; width: 505px;
    color: var(--text);
    font-size: 14.6px; line-height: 20.7px;
  }
  .content p { margin-bottom: 8px; }
  .content h2 {
    color: var(--ink); font-size: 20px; font-weight: 600;
    margin: 17px 0 4px; line-height: 1.2;
  }
  .footer {
    position: absolute; left: 0; top: 967px; width: 821px; height: 193px;
    background: var(--footer-bg);
  }
  .brand {
    position: absolute; left: 57px; top: 80px;
    display: flex; align-items: center; gap: 10px;
    color: var(--ink); font-size: 20px; font-weight: 600;
  }
  .brand-dot { width: 12px; height: 12px; border-radius: 50%; background: var(--accent); }
  .contact {
    position: absolute; left: 268px; top: 26px;
    color: var(--ink); font-size: 16.5px; line-height: 1.45;
  }
  .contact .email { font-size: 19px; margin-bottom: 16px; }
  .contact .email b { font-weight: 700; }
  .contact .name { font-weight: 700; font-size: 15px; margin-bottom: 8px; }
  .contact .tel { margin-top: 6px; }
</style>
</head>
<body>
  <main class="ad">
    <div class="hero" role="img" aria-label="Foto der historischen Praxisfassade mit roten Fensterläden, Holztür, Laternen und Garten"></div>
    <div class="hero-band">
      <div class="hero-title">Hausarztmedizin mit Tiefe</div>
      <div class="hero-sub">– dort, wo man noch echte Grundversorgung lebt</div>
    </div>

    <aside class="intro">
      <p>Ein Ort, der trägt.</p>
      <p>Ein Team, das bleibt.</p>
      <p>Eine Arbeit, die Wertschätzung hat.</p>
      <p class="gap">Manche Orte verändern die Art, wie man arbeitet.</p>
      <p class="gap">Unsere Praxis in Sonnhalden ist so ein Ort.</p>
    </aside>

    <section class="content">
      <p>In einem historischen Gebäude gelegen, mit grosszügigem Ambiente, warmen Vertäfelungen und kunstvoller Wandbemalung, entstehen hier Behandlungsräume von Ruhe und Würde. Kein steriler Praxisalltag, sondern ein Ort, der Gespräche trägt und medizinische Arbeit unterstützt.</p>
      <p>Für diesen besonderen Ort suchen wir eine Hausärztin oder einen Hausarzt, die oder der nicht einfach einen Arbeitsplatz sucht, sondern einen Platz, an dem Medizin menschlich sein darf.</p>
      <h2>Ein Team mit Haltung</h2>
      <p>Sie arbeiten in einem freundlichen, über Jahre gewachsenen Team mit hoher personeller Kontinuität und geringer Fluktuation.</p>
      <h2>Zeit für gute Medizin</h2>
      <p>Unsere Patientinnen und Patienten sind überwiegend gut bis sehr gut situiert, wertschätzend und therapieoffen. Das ermöglicht ruhiges, strukturiertes Arbeiten mit Fokus auf Qualität, Beziehung und nachhaltige Behandlung.</p>
      <h2>Und sonst?</h2>
      <p>Der Praxisalltag ist klar strukturiert, ruhig und verlässlich. Geregelte und in Abstimmung flexible Arbeitszeiten ohne Wochenend- oder Nachtdienste, eine sehr gute leistungsbezogene Vergütung sowie ein respektvoller, wertschätzender Umgang auf Augenhöhe schaffen ein Umfeld, in dem man sich auf die medizinische Arbeit konzentrieren und langfristig wohlfühlen kann.</p>
      <p>Wir freuen uns über eine unkomplizierte Kontaktaufnahme per E-Mail oder Telefon – gerne auch ganz unverbindlich und ohne vollständige Bewerbungsunterlagen.</p>
    </section>

    <footer class="footer">
      <div class="brand"><span class="brand-dot"></span>Praxis Lindenhof</div>
      <div class="contact">
        <div class="email"><b>E-Mail:</b> Melina.Korvath@praxis-lindenhof.ch</div>
        <div class="name">Praxis Lindenhof</div>
        <div>Mühleweg 7</div>
        <div>4890 Sonnhalden</div>
        <div class="tel">Tel: 0621234567</div>
      </div>
    </footer>
  </main>
</body>
</html>
```